Orvel Crest Holdings Ltd
Creative Brief
Dara Kolby
COO
27B Hollin Row, London, E3 9TQ
dk@orvelcrest.co.uk
27b Hollin Row
Just the logo and the company's name on the green background

```html
<!DOCTYPE html>
<html lang="en">
<head>
<meta charset="utf-8">
<title>Orvel Crest Holdings Ltd — Business Card</title>
<link rel="stylesheet" href="https://fonts.googleapis.com/css2?family=Libre+Baskerville:wght@400;700&display=swap">
<style>
  :root {
    --backdrop: #e4e4e2;
    --paper: #ffffff;
    --forest: #3a3e2b;
    --gold: #c39a5c;
    --ink: #2b2b27;
    --cream: #f4f1ea;
  }
  * { box-sizing: border-box; margin: 0; padding: 0; }
  html, body { width: 1200px; height: 670px; overflow: hidden; }
  body {
    background: var(--backdrop);
    font-family: "Libre Baskerville", Georgia, serif;
    position: relative;
  }
  .palette { position: absolute; top: 60px; left: 100px; display: flex; gap: 17px; }
  .swatch { width: 116px; height: 26px; }
  .swatch--gold { background: var(--gold); }
  .swatch--forest { background: var(--forest); }

  .card {
    position: absolute;
    top: 173px;
    width: 500px;
    height: 305px;
  }
  .card--front { left: 96px; background: var(--paper); }
  .card--back { left: 626px; background: var(--forest); }

  .front-mark {
    position: absolute; left: 40px; top: 24px;
    display: flex; flex-direction: column; align-items: center; gap: 8px;
  }
  .front-mark__name {
    color: var(--gold); font-size: 9px; letter-spacing: 2px; font-weight: 400;
  }
  .holder { position: absolute; left: 36px; top: 196px; }
  .holder__name { font-size: 22px; color: var(--ink); font-weight: 400; }
  .holder__role { font-size: 14px; color: var(--gold); margin-top: 9px; letter-spacing: 1px; }

  .divider {
    position: absolute; left: 259px; top: 187px;
    width: 1.5px; height: 97px; background: var(--gold);
  }
  .contacts {
    position: absolute; left: 270px; top: 187px;
    list-style: none; font-size: 11px; font-weight: 700;
    color: var(--ink); line-height: 19px;
  }

  .back-mark {
    position: absolute; left: 0; right: 0; top: 22px;
    display: flex; flex-direction: column; align-items: center;
  }
  .back-mark__name {
    margin-top: 28px; color: var(--cream); font-weight: 400;
    font-size: 44px; letter-spacing: 2px; line-height: 1;
  }
  .back-mark__sub {
    margin-top: 12px; color: var(--cream); font-weight: 400;
    font-size: 13px; letter-spacing: 2px;
  }
</style>
</head>
<body>
  <div class="palette">
    <div class="swatch swatch--gold"></div>
    <div class="swatch swatch--forest"></div>
  </div>

  <section class="card card--front">
    <div class="front-mark">
      <svg width="96" height="96" viewBox="0 0 96 96" aria-hidden="true">
        <circle cx="48" cy="48" r="45" fill="none" stroke="var(--gold)" stroke-width="2"/>
      </svg>
      <span class="front-mark__name">ORVEL CREST</span>
    </div>
    <div class="holder">
      <p class="holder__name">Dara Kolby</p>
      <p class="holder__role">COO</p>
    </div>
    <div class="divider"></div>
    <ul class="contacts">
      <li>+44 (0)20 7946 0321</li>
      <li>+44 (0)77 0090 0412</li>
      <li>dk@orvelcrest.co.uk</li>
      <li>27B Hollin Row, London,</li>
      <li>E3 9TQ</li>
    </ul>
  </section>

  <section class="card card--back">
    <div class="back-mark">
      <svg width="140" height="140" viewBox="0 0 140 140" aria-hidden="true">
        <circle cx="70" cy="70" r="67" fill="none" stroke="var(--gold)" stroke-width="2.5"/>
      </svg>
      <p class="back-mark__name">ORVEL CREST</p>
      <p class="back-mark__sub">HOLDINGS LTD.</p>
    </div>
  </section>
</body>
</html>
```